Car cleaning and lubrication automotive retail label

Designing a modern, trendy car cleaning and lubrication label for the retail automitive business. the label should be suitable for a retail home and garden product range. We are looking for a label that is realistic and colorful. Greens and blues are what we think would fit best for a eco label. We would like to stand out from other similar product ranges by design, meaning that we are looking for an ultra modern, simple, clean and professional design. We are also looking for a new design for the logo, clean and modern. It should include: The 'KALDRIX' logo that can have any color and "Automotive".

Example text for cleaning product (please keep in mind we need a combi cleaning product label that is also suitable for a lubrication label)

The label should have a front and a back:
Front label: Texts and slogans (in dutch):
- Reiniger, ontvetter en polisher
- Bescherming en glans
- Veilig, geconcentreerd en eco friendly
- Milieuvriendelijk
Product name: Stainless Steel Cleaner
Image of car/stainless steel on car
Eco icon
+ Icons explaining the product (cleans stainless steel on car, protection and shine, safe and concentrated, eco friendly, cleaner, degreaser, polisher)

Back label:
Instructions to use
About the product
Remarks
Updates

Target Market(s)

Automotive, car cleaning, car lubrication, car additives

Industry/Entity Type

Automotive

Colors
0692cd
a64599
e33e95
acd037
f04a50
ec1f27
cadf82
33a6d7
33b8a4

Requirements
Must have
• Must have modern colors, cool look, attract customers by an original design

```html
<!DOCTYPE html>
<html lang="nl">
<head>
<meta charset="utf-8">
<title>Stainless Steel Cleaner – Label</title>
<link rel="stylesheet" href="https://fonts.googleapis.com/css2?family=Oswald:wght@600;700&family=Staatliches&display=swap">
<style>
  :root {
    --night: #020b1d;
    --deep: #0a2550;
    --mid: #133a72;
    --glow: #3aa0ff;
    --chrome-light: #f4f6f8;
    --chrome-mid: #9aa0a8;
    --chrome-dark: #4a4f57;
    --text: #ffffff;
    --icon-bg: #0b0b0d;
    --eco-green: #0f5a1c;
  }
  * { margin: 0; padding: 0; box-sizing: border-box; }
  html, body { width: 1034px; height: 1200px; overflow: hidden; background: var(--night); }
  .label {
    position: relative;
    width: 1034px;
    height: 1200px;
    overflow: hidden;
    font-family: "Oswald", sans-serif;
  }
  .car-photo {
    position: absolute;
    inset: 0;
    background:
      radial-gradient(ellipse 60% 30% at 50% 30%, rgba(30,110,170,0.35), transparent 70%),
      radial-gradient(ellipse 90% 55% at 55% 75%, var(--mid), transparent 75%),
      linear-gradient(180deg, var(--night) 0%, var(--deep) 45%, #0e2c5c 70%, #061630 100%);
  }
  .title {
    position: absolute;
    left: 0;
    width: 100%;
    text-align: center;
    font-family: "Staatliches", sans-serif;
    font-weight: 400;
    line-height: 1;
    letter-spacing: 6px;
    background: linear-gradient(180deg, var(--chrome-light) 0%, var(--chrome-mid) 40%, var(--chrome-dark) 55%, var(--chrome-light) 80%, var(--chrome-mid) 100%);
    -webkit-background-clip: text;
    background-clip: text;
    color: transparent;
    filter: drop-shadow(0 3px 4px rgba(0,0,0,0.7));
  }
  .title-line-1 { top: 281px; font-size: 112px; }
  .title-line-2 { top: 424px; font-size: 112px; }
  .horizon-glow {
    position: absolute;
    left: 60px;
    top: 528px;
    width: 914px;
    height: 10px;
    background: radial-gradient(ellipse 50% 50% at 50% 50%, #bfe6ff 0%, var(--glow) 25%, rgba(58,160,255,0.25) 60%, transparent 100%);
    filter: blur(1px);
  }
  .benefits { position: absolute; left: 306px; top: 634px; list-style: none; }
  .benefit { display: flex; align-items: center; height: 56px; margin-bottom: 23px; }
  .benefit-icon {
    width: 56px; height: 56px; border-radius: 50%;
    background: radial-gradient(circle at 35% 30%, #2a2a2e, var(--icon-bg) 60%);
    box-shadow: 0 0 10px 2px rgba(58,160,255,0.75);
    display: flex; align-items: center; justify-content: center;
    flex-shrink: 0;
  }
  .benefit-icon svg { width: 30px; height: 30px; }
  .benefit-text {
    margin-left: 24px;
    color: var(--text);
    font-size: 27px;
    font-weight: 700;
    letter-spacing: 1.6px;
    text-transform: uppercase;
    white-space: nowrap;
  }
  .eco-badge {
    position: absolute;
    left: 771px; top: 982px;
    width: 168px; height: 168px;
    border-radius: 50%;
    border: 2px solid var(--eco-green);
    background: radial-gradient(circle, rgba(15,90,28,0.18), rgba(15,90,28,0.05) 70%);
    opacity: 0.85;
  }
</style>
</head>
<body>
<main class="label">
  <div class="car-photo" role="img" aria-label="Donkerblauwe foto van de voorkant van een luxe auto met verchroomde grille"></div>

  <h1>
    <span class="title title-line-1">Stainless Steel</span>
    <span class="title title-line-2">Cleaner</span>
  </h1>
  <div class="horizon-glow"></div>

  <ul class="benefits">
    <li class="benefit">
      <span class="benefit-icon">
        <svg viewBox="0 0 30 30" fill="#fff"><path d="M11 8 L13 15 L20 17 L13 19 L11 26 L9 19 L2 17 L9 15Z"/><path d="M22 2 L23 6 L27 7 L23 8 L22 12 L21 8 L17 7 L21 6Z"/><path d="M22 18 L23 21 L26 22 L23 23 L22 26 L21 23 L18 22 L21 21Z"/></svg>
      </span>
      <span class="benefit-text">Reiniger, ontvetter en polisher</span>
    </li>
    <li class="benefit">
      <span class="benefit-icon">
        <svg viewBox="0 0 30 30" fill="none" stroke="#fff" stroke-width="2.4"><path d="M15 3 L25 7 V14 C25 21 20 25 15 27 C10 25 5 21 5 14 V7Z"/><path d="M15 7 V23"/></svg>
      </span>
      <span class="benefit-text">Bescherming en glans</span>
    </li>
    <li class="benefit">
      <span class="benefit-icon">
        <svg viewBox="0 0 30 30" fill="#fff"><path d="M15 3 C20 8 20 15 15 20 C10 15 10 8 15 3Z"/><path d="M4 13 C10 13 14 17 14 23 C8 23 4 19 4 13Z"/><path d="M16 23 C18 18 23 17 27 19 C24 24 20 25 16 23Z"/></svg>
      </span>
      <span class="benefit-text">Veilig, geconcentreerd en eco friendly</span>
    </li>
    <li class="benefit">
      <span class="benefit-icon">
        <svg viewBox="0 0 30 30" fill="none" stroke="#fff" stroke-width="1.4"><circle cx="15" cy="19" r="8"/><path d="M7 19 H23"/><path d="M10 14 L13 9 L16 14"/><path d="M15 13 L19 7 L23 14"/><path d="M6 6 H11 M20 5 H26"/></svg>
      </span>
      <span class="benefit-text">Milieuvriendelijk</span>
    </li>
  </ul>

  <div class="eco-badge" role="img" aria-label="Eco-keurmerk"></div>
</main>
</body>
</html>
```